Birchwell Chiropractic, achieve your health goals, get better each day one step at a time

A mobile friendly site, fresh look, easy to navigate, has interface with zq/chirplane, etc. Blog posts. Uses new logo. Content and address to current site is marvintoque.com. The current site will give you scope of project for content. The logo is not the final but close. Will upload final next week.
Convey the concept that heath is a process, it does not just happen. We take steps to achieve what we want in life including health.

Target Market(s)

30 to 70 year old. Needing health care

Industry/Entity Type

Health Care

Coding

Coded - Design and coding required

Number of Pages Required

5+ page

Font styles to use
Sans Serif

Colors

Designer to choose colors to be used in the design.

Requirements
Must have
• mobile friendly, easy to navigate, ZQ/Chirplane interface, blog, room for current content
Nice to have
• potential for commerce, statistics
Should not have
• Same old look and feel as everything else out there

```html
<!DOCTYPE html>
<html lang="en">
<head>
<meta charset="utf-8">
<title>Birchwell Chiropractic</title>
<link href="https://fonts.googleapis.com/css2?family=Poppins:wght@400;500;600;700&family=Open+Sans:wght@400;600;700&display=swap" rel="stylesheet">
<style>
:root{
  --blue:#1e6db3;
  --blue-dark:#174f86;
  --green:#8cc63f;
  --ink:#222;
  --text:#555;
  --light:#f0f0f0;
  --grey-band:#e9e9e9;
  --footer:#1b1b1b;
  --footer-bottom:#111;
  --white:#fff;
}
*{box-sizing:border-box;margin:0;padding:0}
html,body{width:1200px;height:5202px;overflow:hidden}
body{font-family:"Open Sans",Arial,sans-serif;color:var(--text);background:var(--white);font-size:13px;line-height:1.6}
h1,h2,h3,h4{font-family:"Poppins",Arial,sans-serif;color:var(--ink)}
.section{position:relative;width:1200px;overflow:hidden}
.heading{text-align:center;font-size:38px;font-weight:500;letter-spacing:.5px;color:#333}
.heading b{color:var(--blue);font-weight:700}
.heading::after{content:"";display:block;width:70px;height:3px;background:var(--blue);margin:14px auto 0}
.ph{display:block}

/* header */
.site-header{height:115px;background:var(--white)}
.topbar{position:absolute;right:175px;top:0;height:32px;display:flex;gap:28px;align-items:center;background:var(--blue);padding:0 26px;color:#fff;font-size:13px;border-radius:0 0 6px 6px;white-space:nowrap}
.topbar span{display:flex;align-items:center;gap:8px}
.brand{position:absolute;left:125px;top:18px;display:flex;align-items:center;gap:12px}
.brand-mark{width:34px;height:34px;border-radius:50%;background:var(--green)}
.brand-name{font-family:"Poppins",sans-serif;font-weight:700;font-size:30px;color:var(--blue);line-height:1}
.brand-sub{font-family:"Poppins",sans-serif;font-weight:700;font-size:15px;color:var(--blue);line-height:1.2}
.nav{position:absolute;left:430px;top:68px;display:flex;gap:20px;font-family:"Poppins",sans-serif;font-size:13px;font-weight:600;color:#333;white-space:nowrap}
.nav .active{color:var(--blue)}
.leaf{position:absolute;right:35px;top:0;width:55px;height:70px}

/* hero */
.hero{height:595px;background:linear-gradient(180deg,#7fa8c9 0%,#b7cfe0 55%,#8a7a66 80%,#6a5f52 100%)}
.hero-title{position:absolute;left:130px;top:170px;color:#fff;font-family:"Poppins",sans-serif;font-weight:600;font-size:54px;line-height:1.15}
.hero-title span{display:block;font-size:60px;font-weight:700}
.btn-green{display:inline-block;background:var(--green);color:#fff;font-family:"Poppins",sans-serif;font-weight:600;border-radius:22px}
.hero .btn-green{position:absolute;left:133px;top:327px;padding:8px 28px;font-size:18px}
.arrow{position:absolute;top:262px;width:34px;height:34px;border-radius:50%;background:#333;display:flex;align-items:center;justify-content:center}
.hero-curve{position:absolute;left:0;bottom:0;width:1200px;height:80px}

/* distinction */
.distinction{height:555px;background:var(--light)}
.distinction .heading{padding-top:55px}
.video{position:absolute;left:173px;top:185px;width:424px;height:291px;background:linear-gradient(135deg,#1e3f7a,#6a8fc4 50%,#1e3f7a);border:6px solid #fff;box-shadow:0 2px 8px rgba(0,0,0,.2)}
.play{position:absolute;left:50%;top:50%;width:56px;height:56px;margin:-28px 0 0 -28px;border-radius:50%;background:#fff;display:flex;align-items:center;justify-content:center}
.features{position:absolute;left:638px;top:185px;width:440px}
.feature{display:flex;gap:20px;margin-bottom:22px}
.feature-icon{flex:0 0 68px;height:68px;border-radius:50%;border:2px solid var(--blue);display:flex;align-items:center;justify-content:center}
.feature h4{font-size:14px;font-weight:600;color:#333;margin-bottom:4px}
.feature p{font-size:12px;line-height:1.5}

/* treatment */
.treatment{height:833px;background:#fff}
.treatment .heading{padding-top:72px}
.treat-grid{position:absolute;left:132px;top:198px;display:grid;grid-template-columns:repeat(3,294px);gap:28px 27px}
.treat-card{height:243px;position:relative;box-shadow:0 2px 8px rgba(0,0,0,.15)}
.treat-card .ph{height:208px}
.treat-card .label{height:35px;background:var(--green);color:#fff;font-family:"Poppins",sans-serif;font-weight:600;font-size:15px;text-align:center;line-height:35px;text-transform:uppercase}

/* services */
.services{height:527px;background:linear-gradient(180deg,#2f7dc0,#1f62a5)}
.services .heading{padding-top:68px;color:#fff}
.services .heading b{color:#fff}
.services .heading::after{background:#fff}
.service-row{position:absolute;left:152px;top:190px;display:flex;gap:30px}
.service{width:220px;text-align:center;color:#e6f0fa}
.service-icon{width:120px;height:120px;border-radius:50%;border:3px solid #fff;margin:0 auto 18px;display:flex;align-items:center;justify-content:center}
.service h4{color:#fff;font-size:17px;font-weight:600;text-transform:uppercase;margin-bottom:6px}
.service p{font-size:12px;line-height:1.5}
.s-arrow{position:absolute;top:295px}

/* meet */
.meet{height:427px;background:var(--grey-band)}
.meet-photo{position:absolute;left:150px;top:55px;width:300px;height:300px;border-radius:50%;background:linear-gradient(135deg,#d9dde2,#9aa6b2);border:6px solid var(--blue)}
.meet h2{position:absolute;left:493px;top:65px;font-size:38px;font-weight:500;color:#333}
.meet h2 b{color:var(--blue);font-weight:600}
.meet p{position:absolute;left:493px;top:138px;width:570px;font-size:14px;line-height:1.85}
.btn-outline{position:absolute;left:493px;top:328px;border:2px solid #333;border-radius:18px;padding:5px 18px;font-family:"Poppins",sans-serif;font-weight:600;font-size:13px;color:#333}

/* social */
.social{height:631px;background:#fff}
.social-col{position:absolute;top:93px;width:278px}
.social-title{font-family:"Poppins",sans-serif;font-weight:700;font-size:32px;color:var(--blue);height:50px}
.widget{height:370px;border:1px solid #ddd;box-shadow:0 2px 6px rgba(0,0,0,.15);background:#fff;padding:12px}
.widget-head{display:flex;justify-content:space-between;font-size:13px;color:#333;border-bottom:1px solid #eee;padding-bottom:8px;margin-bottom:10px}
.follow{background:var(--blue);color:#fff;font-size:10px;padding:0 6px;border-radius:3px}
.post{display:flex;gap:10px;margin-bottom:14px;font-size:11px;line-height:1.45}
.avatar{flex:0 0 30px;height:30px;border-radius:50%;background:var(--blue)}
.post b{color:#333}
.blog-head{display:flex;justify-content:space-between;align-items:center;font-family:"Poppins",sans-serif;font-size:30px;color:#333;height:50px}
.blog-head b{color:var(--blue)}
.blog-card{border:1px solid #ddd;box-shadow:0 2px 6px rgba(0,0,0,.15);height:355px}
.blog-card .ph{height:180px}
.blog-body{padding:14px}
.blog-body h4{font-size:15px;font-weight:600;color:#333;margin-bottom:6px}
.blog-date{color:var(--blue);font-size:12px;margin-bottom:6px}
.blog-body p{font-size:11px;line-height:1.5}

/* contact */
.contact{height:434px}
.form-side{position:absolute;left:0;top:0;width:560px;height:434px;background:linear-gradient(135deg,#2d82c4,#1a5ea1)}
.form{position:absolute;left:130px;top:40px;width:382px}
.field{height:36px;background:#fff;margin-bottom:14px;font-size:12px;color:#777;padding:8px 10px}
.field.area{height:72px}
.form .btn-green{border-radius:3px;padding:6px 0;width:225px;text-align:center;font-size:15px}
.map{position:absolute;left:560px;top:0;width:640px;height:434px;background:linear-gradient(135deg,#ecebe4,#dfe3e0 60%,#e8e2cf)}

/* testimonials */
.testimonials{height:607px;background:#fff}
.testimonials .heading{padding-top:95px}
.testi-row{position:absolute;left:148px;top:283px;display:flex;gap:36px}
.testi{width:276px;text-align:center}
.testi-card{position:relative;height:208px;padding:68px 26px 0;background:#fff;box-shadow:0 2px 10px rgba(0,0,0,.18);font-size:12px;line-height:1.55}
.testi-photo{position:absolute;left:50%;top:-42px;margin-left:-42px;width:84px;height:84px;border-radius:50%;background:linear-gradient(135deg,#c9b6a5,#8b7461);border:4px solid #fff;box-shadow:0 1px 4px rgba(0,0,0,.2)}
.testi-name{margin-top:22px;color:var(--blue);font-family:"Poppins",sans-serif;font-size:14px;line-height:1.4}
.stars{color:#f39c12;letter-spacing:2px;font-size:14px}

/* footer */
.footer-curve{height:86px;background:#fff}
.footer{height:295px;background:var(--footer);color:#ccc}
.footer h4{color:#fff;font-size:20px;font-weight:500;text-transform:uppercase;margin-bottom:20px}
.f-col{position:absolute;top:36px}
.f-line{display:flex;gap:12px;font-size:13px;margin-bottom:14px}
.f-links{list-style:none;font-size:13px;line-height:1.75}
.f-links li::before{content:"";display:inline-block;width:6px;height:6px;background:#fff;border-radius:50%;margin-right:10px;vertical-align:middle}
.news p{font-size:12px;line-height:1.5;margin-bottom:14px}
.news .field{width:250px;height:34px;margin-bottom:12px}
.news .btn-green{border-radius:3px;padding:4px 14px;font-size:13px}
.f-brand{position:absolute;left:870px;top:100px;text-align:center}
.f-social{display:flex;gap:8px;justify-content:center;margin-top:14px}
.f-social span{width:26px;height:26px;border-radius:50%;border:2px solid #fff}
.copyright{height:97px;background:var(--footer-bottom);color:#aaa;font-size:13px;text-align:center;line-height:90px}
</style>
</head>
<body>

<header class="section site-header">
  <div class="brand">
    <span class="brand-mark"></span>
    <div><div class="brand-name">Birchwell</div><div class="brand-sub">Chiropractic</div></div>
  </div>
  <div class="topbar">
    <span><svg width="14" height="14" viewBox="0 0 24 24"><path fill="#fff" d="M6.6 10.8a15 15 0 0 0 6.6 6.6l2.2-2.2c.3-.3.7-.4 1-.2 1.1.4 2.3.6 3.6.6.6 0 1 .4 1 1V20c0 .6-.4 1-1 1C10.6 21 3 13.4 3 4c0-.6.4-1 1-1h3.5c.6 0 1 .4 1 1 0 1.3.2 2.5.6 3.6.1.3 0 .7-.2 1z"/></svg>806.555.0148</span>
    <span><svg width="14" height="12" viewBox="0 0 24 20"><rect x="1" y="1" width="22" height="18" fill="none" stroke="#fff" stroke-width="2"/><path d="M1 2l11 9 11-9" fill="none" stroke="#fff" stroke-width="2"/></svg>info@marvintoque.com</span>
  </div>
  <nav class="nav">
    <span class="active">HOME</span><span>MEET DR. VARNELL</span><span>SERVICES</span><span>TESTIMONIALS</span><span>FAQS</span><span>RESOURCES</span><span>CONTACT</span>
  </nav>
  <svg class="leaf" viewBox="0 0 70 90"><path d="M0 0h70v40c0 28-20 45-35 50C20 85 0 68 0 40z" fill="var(--green)"/></svg>
</header>

<section class="section hero" role="img" aria-label="Woman running outdoors with her spine highlighted, mountain and sky behind">
  <h1 class="hero-title">Birchwell<span>CHIROPRACTIC</span></h1>
  <span class="btn-green">make an appointment</span>
  <span class="arrow" style="left:64px"><svg width="12" height="12" viewBox="0 0 12 12"><path d="M8 1L3 6l5 5" stroke="#fff" stroke-width="2" fill="none"/></svg></span>
  <span class="arrow" style="right:64px"><svg width="12" height="12" viewBox="0 0 12 12"><path d="M4 1l5 5-5 5" stroke="#fff" stroke-width="2" fill="none"/></svg></span>
  <svg class="hero-curve" viewBox="0 0 1200 80" preserveAspectRatio="none">
    <path d="M0 40 Q600 100 1200 10 L1200 80 L0 80z" fill="var(--blue)"/>
    <path d="M0 55 Q600 110 1200 28 L1200 80 L0 80z" fill="var(--green)"/>
    <path d="M0 66 Q600 118 1200 44 L1200 80 L0 80z" fill="var(--light)"/>
  </svg>
</section>

<section class="section distinction">
  <h2 class="heading"><b>OUR</b> DISTINCTION</h2>
  <div class="video" role="img" aria-label="X-ray of a human spine and ribcage">
    <span class="play"><svg width="20" height="22" viewBox="0 0 20 22"><path d="M2 1l17 10L2 21z" fill="#333"/></svg></span>
  </div>
  <div class="features">
    <div class="feature"><span class="feature-icon"><svg width="30" height="30" viewBox="0 0 30 30"><rect x="6" y="4" width="18" height="22" fill="none" stroke="var(--blue)" stroke-width="2"/><path d="M10 11h10M10 16h10M10 21h6" stroke="var(--blue)" stroke-width="2"/></svg></span><div><h4>QUIS AUTEM VEL EUM IURE</h4><p>Sed ut perspiciatis unde omnis iste natus error sit totam accusantium doloremque laudantium, totam rem</p></div></div>
    <div class="feature"><span class="feature-icon"><svg width="30" height="30" viewBox="0 0 30 30"><circle cx="15" cy="15" r="6" fill="none" stroke="var(--blue)" stroke-width="2"/><path d="M15 3v5M15 22v5M3 15h5M22 15h5" stroke="var(--blue)" stroke-width="2"/></svg></span><div><h4>QUIS AUTEM VEL EUM IURE</h4><p>Sed ut perspiciatis unde omnis iste natus error sit totam accusantium doloremque laudantium, totam rem</p></div></div>
    <div class="feature"><span class="feature-icon"><svg width="30" height="30" viewBox="0 0 30 30"><circle cx="15" cy="11" r="5" fill="none" stroke="var(--blue)" stroke-width="2"/><path d="M6 26c1-6 5-8 9-8s8 2 9 8" fill="none" stroke="var(--blue)" stroke-width="2"/></svg></span><div><h4>QUIS AUTEM VEL EUM IURE</h4><p>Sed ut perspiciatis unde omnis iste natus error sit totam accusantium doloremque laudantium, totam rem</p></div></div>
  </div>
</section>

<section class="section treatment">
  <h2 class="heading"><b>OUR</b> TREATMENT</h2>
  <div class="treat-grid">
    <div class="treat-card"><div class="ph" role="img" aria-label="Woman holding her head in pain" style="background:linear-gradient(135deg,#8a7a6c,#c7b8a8)"></div><div class="label">Headaches</div></div>
    <div class="treat-card"><div class="ph" role="img" aria-label="Person holding a sore shoulder" style="background:linear-gradient(135deg,#c59a82,#e9d2c2)"></div><div class="label">Shoulder Pain</div></div>
    <div class="treat-card"><div class="ph" role="img" aria-label="Person holding lower back" style="background:linear-gradient(135deg,#d7c7b5,#a88b72)"></div><div class="label">Lower Back Pain</div></div>
    <div class="treat-card"><div class="ph" role="img" aria-label="Person holding hip in pain" style="background:linear-gradient(135deg,#b4453b,#e0a890)"></div><div class="label">Hip &amp; Leg Pain</div></div>
    <div class="treat-card"><div class="ph" role="img" aria-label="Woman rubbing her neck" style="background:linear-gradient(135deg,#e3b8a0,#b0553f)"></div><div class="label">Neck Pain</div></div>
    <div class="treat-card"><div class="ph" role="img" aria-label="Man on a field holding his knee" style="background:linear-gradient(135deg,#9ec3e0,#6fa04c)"></div><div class="label">Knee Pain</div></div>
  </div>
</section>

<section class="section services">
  <h2 class="heading"><b>OUR</b> SERVICES</h2>
  <svg class="s-arrow" style="left:88px" width="14" height="24" viewBox="0 0 14 24"><path d="M12 2L2 12l10 10" stroke="#fff" stroke-width="2" fill="none"/></svg>
  <svg class="s-arrow" style="right:88px" width="14" height="24" viewBox="0 0 14 24"><path d="M2 2l10 10L2 22" stroke="#fff" stroke-width="2" fill="none"/></svg>
  <div class="service-row">
    <div class="service"><div class="service-icon"><svg width="50" height="60" viewBox="0 0 50 60"><rect x="18" y="4" width="14" height="10" rx="3" fill="#fff"/><rect x="18" y="18" width="14" height="10" rx="3" fill="#fff"/><rect x="18" y="32" width="14" height="10" rx="3" fill="#fff"/><rect x="18" y="46" width="14" height="10" rx="3" fill="#fff"/></svg></div><h4>Chiropractic</h4><p>Sed ut perspiciatis unde omnis iste natus error sit voluptatem accusantium doloremque laudantium, totam rem aperiam</p></div>
    <div class="service"><div class="service-icon"><svg width="56" height="50" viewBox="0 0 56 50"><circle cx="14" cy="12" r="6" fill="#fff"/><rect x="6" y="24" width="46" height="8" fill="#fff"/><path d="M40 4l-6 18" stroke="#fff" stroke-width="3"/><path d="M10 40h36" stroke="#fff" stroke-width="3"/></svg></div><h4>Acupuncture</h4><p>Sed ut perspiciatis unde omnis iste natus error sit voluptatem accusantium doloremque laudantium, totam rem aperiam</p></div>
    <div class="service"><div class="service-icon"><svg width="50" height="56" viewBox="0 0 50 56"><path d="M25 54V20" stroke="#fff" stroke-width="3"/><path d="M25 30C12 28 8 18 10 8c12 2 16 12 15 22zM25 24c12-2 16-12 15-20-12 2-16 10-15 20z" fill="#fff"/></svg></div><h4>Homeopathy</h4><p>Sed ut perspiciatis unde omnis iste natus error sit voluptatem accusantium doloremque laudantium, totam rem aperiam</p></div>
    <div class="service"><div class="service-icon"><svg width="56" height="50" viewBox="0 0 56 50"><circle cx="12" cy="26" r="6" fill="#fff"/><rect x="20" y="24" width="32" height="8" rx="3" fill="#fff"/><circle cx="34" cy="10" r="5" fill="#fff"/><path d="M34 16v8M4 38h48" stroke="#fff" stroke-width="3"/></svg></div><h4>Massage</h4><p>Sed ut perspiciatis unde omnis iste natus error sit voluptatem accusantium doloremque laudantium, totam rem aperiam</p></div>
  </div>
</section>

<section class="section meet">
  <div class="meet-photo" role="img" aria-label="Portrait of the doctor and his wife"></div>
  <h2>MEET <b>DR. VARNELL</b></h2>
  <p>Sed ut perspiciatis unde omnis iste natus error sit voluptatem accusantium doloremque laudantium, totam rem aperiam, eaque ipsa quae ab illo inventore veritatis et quasi architecto beatae vitae dicta sunt explicabo. Nemo enim ipsam voluptatem quia voluptas sit aspernatur aut odit aut fugit, sed quia consequuntur magni dolores eos qui ratione voluptatem sequi nesciunt. Neque porro quisquam</p>
  <span class="btn-outline">READ MORE</span>
</section>

<section class="section social">
  <div class="social-col" style="left:132px">
    <div class="social-title">chirplane</div>
    <div class="widget">
      <div class="widget-head"><span>Chirplane Updates</span><span class="follow">Follow</span></div>
      <div class="post"><span class="avatar"></span><div><b>Birchwell Chiropractic</b><br>@birchwellchiro<br>Lorem ipsum dolor sit amet, consectetur adip elit, sed do eiusmod tempor incididunt ut labore et dolore magna aliqua.</div></div>
      <div class="post"><span class="avatar"></span><div><b>Birchwell Chiropractic</b><br>@birchwellchiro<br>Lorem ipsum dolor sit amet, consectetur adip elit, sed do eiusmod tempor incididunt ut labore et dolore magna aliqua.</div></div>
    </div>
  </div>
  <div class="social-col" style="left:447px">
    <div class="social-title" style="color:var(--blue-dark)">zq</div>
    <div class="widget">
      <div class="widget-head"><span>ZQ Updates</span></div>
      <div class="post"><span class="avatar"></span><div><b>Birchwell Chiropractic</b><br>Dec. Read · 4:10 AM</div></div>
      <div class="ph" role="img" aria-label="Clinic building exterior with sign" style="height:150px;background:linear-gradient(180deg,#a8c3dc,#7d5a48)"></div>
      <p style="font-size:11px;margin-top:10px;line-height:1.5">Sed ut perspiciatis unde omnis iste natus error sit voluptatem accusantium doloremque laudantium, totam rem aperiam.</p>
    </div>
  </div>
  <div class="social-col" style="left:762px;width:305px">
    <div class="blog-head"><span>LATEST <b>BLOG</b></span><svg width="26" height="14" viewBox="0 0 26 14"><path d="M8 2L3 7l5 5M18 2l5 5-5 5" stroke="var(--blue)" stroke-width="2" fill="none"/></svg></div>
    <div class="blog-card">
      <div class="ph" role="img" aria-label="Hands giving a back massage" style="background:linear-gradient(135deg,#c89878,#6e4534)"></div>
      <div class="blog-body">
        <h4>Nulla ut diam ornare, aliquam</h4>
        <div class="blog-date">JUNE 20, 2018</div>
        <p>Nunc rutrum ipsum aliquet quam sed commodo ante. Nam at dui a leo luctus consectetur quis eget libero. Suspendisse potenti. Pellentesque habitant morbi tristique senectus</p>
      </div>
    </div>
  </div>
</section>

<section class="section contact">
  <div class="form-side">
    <div class="form">
      <div class="field">First Name</div>
      <div class="field">Last Name</div>
      <div class="field">Email Address</div>
      <div class="field">Phone Number</div>
      <div class="field area">Message</div>
      <span class="btn-green">SUBMIT</span>
    </div>
  </div>
  <div class="map" role="img" aria-label="Street map showing the clinic location in Amarillo"></div>
</section>

<section class="section testimonials">
  <h2 class="heading" style="color:var(--blue);font-weight:600">CLIENT TESTIMONIALS</h2>
  <div class="testi-row">
    <div class="testi"><div class="testi-card"><span class="testi-photo" role="img" aria-label="Client portrait"></span>Sed ut perspiciatis unde omnis iste natus error sit voluptatem accusantium doloremque laudantium, totam rem aperiam, eaque ipsa</div><div class="testi-name">Tariq Dunmore<br>Birchwell Chiropractic</div><div class="stars">★★★★★</div></div>
    <div class="testi"><div class="testi-card"><span class="testi-photo" role="img" aria-label="Client portrait"></span>Sed ut perspiciatis unde omnis iste natus error sit voluptatem accusantium doloremque laudantium, totam rem aperiam, eaque ipsa</div><div class="testi-name">Tariq Dunmore<br>Birchwell Chiropractic</div><div class="stars">★★★★★</div></div>
    <div class="testi"><div class="testi-card"><span class="testi-photo" role="img" aria-label="Client portrait"></span>Sed ut perspiciatis unde omnis iste natus error sit voluptatem accusantium doloremque laudantium, totam rem aperiam, eaque ipsa</div><div class="testi-name">Tariq Dunmore<br>Birchwell Chiropractic</div><div class="stars">★★★★★</div></div>
  </div>
</section>

<div class="section footer-curve">
  <svg width="1200" height="86" viewBox="0 0 1200 86" preserveAspectRatio="none">
    <path d="M0 30 Q600 110 1200 20 L1200 86 L0 86z" fill="var(--green)"/>
    <path d="M0 40 Q600 120 1200 30 L1200 86 L0 86z" fill="var(--blue)"/>
    <path d="M0 50 Q600 128 1200 42 L1200 86 L0 86z" fill="var(--footer)"/>
  </svg>
</div>

<footer class="section footer">
  <div class="f-col" style="left:123px">
    <h4>Contact Us</h4>
    <div class="f-line"><svg width="14" height="18" viewBox="0 0 14 18"><path d="M7 1a6 6 0 0 0-6 6c0 5 6 10 6 10s6-5 6-10a6 6 0 0 0-6-6z" fill="none" stroke="#fff" stroke-width="1.5"/><circle cx="7" cy="7" r="2" fill="#fff"/></svg><span>4870 Larkfield Road West<br>Amarillo, TX 79106</span></div>
    <div class="f-line"><svg width="14" height="14" viewBox="0 0 24 24"><path fill="#fff" d="M6.6 10.8a15 15 0 0 0 6.6 6.6l2.2-2.2c.3-.3.7-.4 1-.2 1.1.4 2.3.6 3.6.6.6 0 1 .4 1 1V20c0 .6-.4 1-1 1C10.6 21 3 13.4 3 4c0-.6.4-1 1-1h3.5c.6 0 1 .4 1 1 0 1.3.2 2.5.6 3.6.1.3 0 .7-.2 1z"/></svg><span>Phone : 806.555.0148</span></div>
    <div class="f-line"><svg width="14" height="12" viewBox="0 0 24 20"><rect x="1" y="1" width="22" height="18" fill="none" stroke="#fff" stroke-width="2"/><path d="M1 2l11 9 11-9" fill="none" stroke="#fff" stroke-width="2"/></svg><span>Email: info@marvintoque.com</span></div>
  </div>
  <div class="f-col" style="left:388px">
    <h4>Quick Links</h4>
    <ul class="f-links"><li>Home</li><li>Meet Dr. Varnell</li><li>Other Services</li><li>Testimonials</li><li>Faqs</li><li>Resources</li><li>Contact</li></ul>
  </div>
  <div class="f-col news" style="left:563px">
    <h4>Sign Up For Newsletter</h4>
    <p>Receive our newest updates and<br>health tips delivered to your inbox</p>
    <div class="field">Email</div>
    <span class="btn-green">SUBSCRIBE</span>
  </div>
  <div class="f-brand">
    <div style="display:flex;align-items:center;gap:10px"><span class="brand-mark"></span><span class="brand-name">Birchwell</span></div>
    <div class="f-social"><span></span><span></span><span></span><span></span></div>
  </div>
</footer>
<div class="section copyright">2018 © Copyrights Birchwell Chiropractic. All Rights Reserved</div>

</body>
</html>
```